New more attractive design for an old tired look that is high tech but inviting

Need a more modern eye catching design. We are and I/T and MSP and we need a new look. Need a call to action on each page. Needs to be in WordPress. Existing site is brivanoqe.com. Needs to work on phones and tablets. The default home page should present us as an MSP/MSSP and direct the viewer to our services we offer.
Updates

Current deadline assigned at project inception has passed before project started

Need extra days to review

Target Market(s)

Our target market is other businesses. We do not target residential customers.

Industry/Entity Type

Business to Business oriented

Coding

Coded - Design and coding required

Number of Pages Required

5+ page

Font styles to use
Sans Serif

Requirements
Must have
• Must have a current relevant design with a call to action on each page.
Nice to have
• Dark background high tech look with people to make it attractive

```html
<!DOCTYPE html>
<html lang="en">
<head>
<meta charset="utf-8">
<title>Corvalen Systems – Managed IT &amp; Security</title>
<link href="https://fonts.googleapis.com/css2?family=Poppins:wght@300;400;500;600;700&display=swap" rel="stylesheet">
<style>
:root{
  --red:#e01e26;
  --red-dark:#b3121a;
  --ink:#1d1d1f;
  --body:#444;
  --muted:#666;
  --white:#fff;
  --navy:#0b1f3a;
  --blue:#14507e;
  --footer:#121212;
  --line:#f4d6e6;
}
*{box-sizing:border-box;margin:0;padding:0}
html,body{width:1200px;height:3549px;overflow:hidden}
body{position:relative;font-family:'Poppins',sans-serif;color:var(--ink);background:var(--white)}
.abs{position:absolute}

/* header */
.site-header{position:absolute;left:0;top:0;width:1200px;height:72px;background:var(--white);z-index:5}
.brand{position:absolute;display:flex;align-items:center;gap:8px;font-weight:700;color:var(--ink);white-space:nowrap}
.brand-mark{width:10px;height:10px;background:var(--red);flex:none}
.site-header .brand{left:116px;top:20px;font-size:24px}
.main-nav{position:absolute;left:666px;top:24px;display:flex;gap:31px;font-size:14px;font-weight:500}
.main-nav a{color:var(--ink);text-decoration:none}
.main-nav a.current{color:var(--red)}
.btn-contact{position:absolute;left:947px;top:10px;width:141px;height:47px;background:var(--red);color:var(--white);font-size:15px;font-weight:700;display:flex;align-items:center;justify-content:center;border-radius:2px}

/* hero */
.hero{position:absolute;left:0;top:72px;width:1200px;height:790px}
.hero-photo{position:absolute;inset:0;background:linear-gradient(100deg,#0a1a33 0%,#123f6b 30%,#1c6a9a 55%,#0f3f66 80%,#0a2240 100%);clip-path:polygon(0 0,100% 0,100% 620px,835px 778px,0 628px)}
.hero-title{position:absolute;left:114px;top:210px;font-size:47px;color:var(--white);font-weight:300;letter-spacing:-.5px}
.hero-title strong{font-weight:700}
.hero-text{position:absolute;left:118px;top:282px;width:372px;font-size:17px;line-height:24px;letter-spacing:-.2px;color:var(--white)}
.btn{position:absolute;display:flex;align-items:center;justify-content:center;font-weight:600;border-radius:4px}
.btn-primary{left:118px;top:374px;width:124px;height:46px;background:var(--red);color:var(--white);font-size:15px}
.btn-outline-light{left:263px;top:374px;width:149px;height:46px;border:2px solid var(--red);color:var(--white);font-size:15px}
.slider-dots{position:absolute;left:122px;top:559px;display:flex;gap:8px}
.slider-dots span{width:14px;height:14px;border-radius:50%;border:1.5px solid #cfe3f5}
.slider-dots span.active{background:var(--red);border-color:var(--red)}
.hero-edge{position:absolute;left:0;top:0}

/* services */
.section-title{position:absolute;width:1200px;text-align:center;font-weight:700;color:#2a2a2a}
.section-title span{color:var(--red)}
.services-title{top:930px;font-size:42px}
.timeline{position:absolute;left:0;top:0}
.service{position:absolute}
.service h3{font-size:21px;font-weight:600;color:var(--ink)}
.service .sub{font-size:15px;color:var(--ink);line-height:23px}
.service p{font-size:11.5px;line-height:19px;color:var(--body)}
.service.left{text-align:right;right:738px}
.service.right{left:762px;width:320px}
.service.right p{text-align:justify}
.service.left p.just{text-align:justify;text-align-last:right}
.btn-learn{display:inline-flex;align-items:center;justify-content:center;width:117px;height:33px;border:1.5px solid #333;border-radius:3px;font-size:10.5px;font-weight:600;color:var(--red);margin-top:14px}
.diamond{position:absolute;width:70px;height:70px;background:var(--red);transform:rotate(45deg)}
.diamond-icon{position:absolute;width:46px;height:46px}

/* about */
.about{position:absolute;left:0;top:1848px;width:1200px;height:533px;overflow:hidden}
.about-bg{position:absolute;inset:0;background:linear-gradient(90deg,var(--red) 0%,var(--red) 55%,#c63122 62%,#8a5a3a 72%,#6f6552 85%,#3f3a30 100%)}
.about-photo{position:absolute;left:716px;top:0;width:484px;height:533px;background:linear-gradient(90deg,rgba(224,30,38,0) 0%,rgba(150,110,70,.55) 30%,rgba(95,90,70,.8) 70%,rgba(60,50,40,.9) 100%)}
.stat{position:absolute;right:1025px;font-size:15px;font-weight:600;color:var(--white)}
.stat-band{position:absolute;left:0;top:2129px;width:220px;height:41px;background:linear-gradient(90deg,rgba(150,10,15,0),#a90d16)}
.about-divider{position:absolute;left:220px;top:1944px;width:1.5px;height:352px;background:rgba(255,255,255,.8)}
.about-title{position:absolute;left:234px;top:1995px;font-size:35px;font-weight:700;color:var(--white);letter-spacing:-.5px;white-space:nowrap}
.about-text{position:absolute;left:270px;top:2055px;width:406px;font-size:13px;line-height:21.8px;color:var(--white);text-align:justify;text-align-last:right}
.btn-outline-white{position:absolute;left:553px;top:2236px;width:124px;height:34px;border:1.5px solid var(--white);color:var(--white);font-size:11px;font-weight:600;display:flex;align-items:center;justify-content:center;border-radius:3px}

/* contact */
.contact-title{top:2470px;font-size:36px;font-weight:300;color:#2a2a2a}
.contact-title strong{font-weight:700}
.title-rule{position:absolute;left:557px;top:2530px;width:86px;height:3px;background:var(--red)}
.contact-sub{position:absolute;width:1200px;top:2554px;text-align:center;font-size:17px;font-weight:500;color:#333}
.contact-photo{position:absolute;left:0;top:2742px;width:1200px;height:411px;background:linear-gradient(90deg,#8ea7c4 0%,#c9b6a4 30%,#a2b9cf 55%,#c7a78b 75%,#6f86a0 100%);opacity:.8}
.contact-photo::after{content:"";position:absolute;inset:0;background:linear-gradient(180deg,#fff 0%,rgba(255,255,255,.3) 45%,rgba(255,255,255,.1) 100%)}
.form-card{position:absolute;left:156px;top:2621px;width:580px;height:390px;background:var(--white);border-radius:0 0 0 34px;box-shadow:0 6px 24px rgba(0,0,0,.12)}
.form-card h4{position:absolute;left:22px;top:18px;font-size:22px;font-weight:500;color:#333}
.field{position:absolute;width:220px;border-bottom:2px solid #f2b9bc;padding-bottom:10px}
.field label{display:block;font-size:11px;color:#777}
.field div{font-size:13px;color:#222;margin-top:2px}
.btn-send{position:absolute;left:438px;top:276px;width:66px;height:66px;border-radius:50%;background:#2b2b2b}
.info-card{position:absolute;left:689px;top:2621px;width:355px;height:390px;background:var(--red);border-radius:0 34px 0 34px;color:var(--white)}
.info-card h4{position:absolute;left:31px;top:22px;font-size:22px;font-weight:600}
.info-row{position:absolute;left:31px;display:flex;align-items:center;gap:20px;font-weight:600;white-space:nowrap}
.social{position:absolute;top:296px;width:28px;height:28px;border:1.5px solid rgba(255,255,255,.85);border-radius:50%}

/* footer */
.site-footer{position:absolute;left:0;top:3153px;width:1200px;height:396px;background:var(--footer);color:var(--white)}
.site-footer .brand{left:196px;top:163px;font-size:21px;color:var(--white)}
.footer-col{position:absolute;top:72px}
.footer-col h5{font-size:20px;font-weight:600}
.footer-col .rule{width:70px;height:3px;background:var(--red);margin:6px 0 14px}
.footer-col ul{list-style:none;font-size:13px;line-height:26px}
.footer-rule{position:absolute;left:111px;top:303px;width:978px;height:1px;background:#2c2c2c}
.copyright{position:absolute;left:111px;top:336px;font-size:13px}
.legal{position:absolute;left:895px;top:336px;font-size:13px;display:flex;gap:34px}
.to-top{position:absolute;left:1127px;top:275px}
.ver{position:absolute;left:1126px;top:339px;font-size:11px;font-weight:600}
</style>
</head>
<body>

<header class="site-header">
  <div class="brand"><span class="brand-mark"></span>Corvalen Systems</div>
  <nav class="main-nav">
    <a class="current">Home</a><a>About</a><a>Services</a><a>Blog</a>
  </nav>
  <div class="btn-contact">CONTACT US</div>
</header>

<section class="hero">
  <div class="hero-photo" role="img" aria-label="Engineers working at computers in a blue-lit data center server room"></div>
  <svg class="hero-edge" width="1200" height="790" viewBox="0 0 1200 790">
    <polygon points="0,620 0,642 600,752 640,752" fill="#e01e26"/>
    <polygon points="935,752 955,752 1200,650 1200,620" fill="#e01e26"/>
  </svg>
  <h1 class="hero-title">Data <strong>Center Services</strong></h1>
  <p class="hero-text">We offer colocation, virtualization, storage as a service and disaster recovery out of our own enterprise-grade data center.</p>
  <div class="btn btn-primary">GET STARTED</div>
  <div class="btn btn-outline-light">QUICK SUPPORT</div>
  <div class="slider-dots"><span></span><span></span><span class="active"></span></div>
</section>

<h2 class="section-title services-title">Our <span>Services</span></h2>

<svg class="timeline" width="1200" height="1800" viewBox="0 0 1200 1800">
  <polyline points="580,1016 610,1046 640,1016" fill="none" stroke="#f4d6e6" stroke-width="4"/>
  <line x1="610" y1="1046" x2="610" y2="1768" stroke="#f4d6e6" stroke-width="4"/>
  <g fill="none" stroke="#e01e26" stroke-width="4">
    <path d="M610 1060 V1110 Q610 1127 593 1127 H552"/>
    <path d="M610 1160 V1218 Q610 1235 627 1235 H668"/>
    <path d="M610 1310 V1358 Q610 1375 593 1375 H554"/>
    <path d="M610 1410 V1457 Q610 1474 627 1474 H668"/>
    <path d="M610 1560 V1606 Q610 1623 593 1623 H554"/>
  </g>
</svg>

<div class="diamond" style="left:482px;top:1092px"></div>
<svg class="diamond-icon" style="left:494px;top:1104px" viewBox="0 0 46 46" fill="none" stroke="#fff" stroke-width="1.6"><path d="M23 8 L35 13 V23 Q35 33 23 38 Q11 33 11 23 V13 Z"/><rect x="18" y="21" width="10" height="8"/><path d="M20 21 V18 Q23 14 26 18 V21"/></svg>
<div class="diamond" style="left:668px;top:1200px"></div>
<svg class="diamond-icon" style="left:680px;top:1212px" viewBox="0 0 46 46" fill="none" stroke="#fff" stroke-width="1.6"><circle cx="23" cy="23" r="14"/><ellipse cx="23" cy="23" rx="6" ry="14"/><line x1="9" y1="23" x2="37" y2="23"/></svg>
<div class="diamond" style="left:484px;top:1340px"></div>
<svg class="diamond-icon" style="left:496px;top:1352px" viewBox="0 0 46 46" fill="none" stroke="#fff" stroke-width="1.6"><rect x="10" y="11" width="26" height="18"/><rect x="15" y="15" width="16" height="10"/><line x1="23" y1="29" x2="23" y2="35"/><line x1="16" y1="35" x2="30" y2="35"/></svg>
<div class="diamond" style="left:668px;top:1439px"></div>
<svg class="diamond-icon" style="left:680px;top:1451px" viewBox="0 0 46 46" fill="none" stroke="#fff" stroke-width="1.6"><path d="M23 9 L37 35 H9 Z"/><path d="M24 16 L19 26 H25 L22 32"/></svg>
<div class="diamond" style="left:484px;top:1588px"></div>
<svg class="diamond-icon" style="left:496px;top:1600px" viewBox="0 0 46 46" fill="none" stroke="#fff" stroke-width="1.6"><circle cx="26" cy="19" r="6"/><circle cx="26" cy="19" r="2"/><path d="M10 30 H17 L22 33 H32 L36 29"/></svg>

<div class="service left" style="top:1050px;width:340px">
  <h3>Cybersecurity</h3>
  <div class="sub">Enterprise-grade cybersecurity — without<br>the enterprise price tag.</div>
  <p style="margin-top:10px">60% of small businesses hit by a cyberattack go out of<br>business within 6 months. But enterprise-level security has<br>always been out of reach — until now.</p>
  <div class="btn-learn">LEARN MORE</div>
</div>

<div class="service right" style="top:1124px">
  <h3>Managed Networks for MDUs</h3>
  <div class="sub" style="font-size:14px;font-weight:500">Student Housing Complexes</div>
  <p style="margin-top:6px">High speed internet is now the number one amenity for multi-dwelling units. It needs to be fast, always online and have excellent coverage around the clock. It must also support a growing number of connections as more devices become Wi-Fi enabled. It's no longer a luxury. It's a necessity.</p>
  <div class="btn-learn">LEARN MORE</div>
</div>

<div class="service left" style="top:1302px;width:345px">
  <h3>Colocation &amp; Virtualization</h3>
  <p class="just" style="margin-top:10px">Corvalen Systems offers a full suite of data center services through our VaultFrame® brand. We work with your organization to develop a solution to meet the unique needs of your business. Our goal is to ensure the confidentiality, integrity and availability of your data around the clock.</p>
  <div class="btn-learn">LEARN MORE</div>
</div>

<div class="service right" style="top:1400px">
  <h3>Low Voltage Wiring</h3>
  <div class="sub" style="font-size:14px;font-weight:500">A Full Range of Low Voltage Solutions</div>
  <p style="margin-top:6px">To keep everyone connected with the outside world, modern buildings run on many different technologies. All of these systems must communicate over the right cabling installed the right way. Our meticulous low voltage technicians have years of experience from projects large to small.</p>
  <div class="btn-learn">LEARN MORE</div>
</div>

<div class="service left" style="top:1550px;width:300px">
  <h3>Office IT Support</h3>
  <div class="sub" style="margin-top:8px;line-height:26px">Managed IT<br>Troubleshooting<br>Staff Augmentation<br>Managed Security</div>
  <div class="btn-learn">LEARN MORE</div>
</div>

<section class="about">
  <div class="about-bg"></div>
  <div class="about-photo" role="img" aria-label="Two founders working at computers in a sunlit garage office"></div>
</section>
<div class="stat-band"></div>
<div class="stat" style="top:2018px">22 years in business</div>
<div class="stat" style="top:2080px">2 owners</div>
<div class="stat" style="top:2139px">1 location</div>
<div class="stat" style="top:2200px">11 employees</div>
<div class="about-divider"></div>
<h2 class="about-title">About Corvalen Systems</h2>
<p class="about-text">Like most great businesses Corvalen Systems began in a garage during the summer of 1995 in Ashford, SC. It was a part time venture by Marek Holloway and his business partner Dale Pruitt. They had discovered an opportunity in technology sales and service after a combined 30 years at Tallbrook Power in information technology. By 2000, the two set out on their own and were working on the venture full-time.</p>
<div class="btn-outline-white">LEARN MORE</div>

<h2 class="section-title contact-title">Contact <strong>Us</strong></h2>
<div class="title-rule"></div>
<p class="contact-sub">Let's Build Something Powerful Together</p>
<div class="contact-photo" role="img" aria-label="Group of colleagues smiling around a laptop"></div>

<div class="form-card">
  <h4>Send us a Message</h4>
  <svg class="abs" style="left:462px;top:22px" width="48" height="26" viewBox="0 0 48 26" fill="none" stroke="#333" stroke-width="1.5"><rect x="16" y="3" width="30" height="20" fill="#fde3c8"/><path d="M16 3 L31 14 L46 3"/><line x1="2" y1="9" x2="12" y2="9"/><line x1="5" y1="14" x2="12" y2="14"/><line x1="2" y1="19" x2="12" y2="19"/></svg>
  <div class="field" style="left:22px;top:70px"><label>Your Name</label><div>Evan Marlow</div></div>
  <div class="field" style="left:272px;top:70px"><label>Email Address</label><div>evan@marlowmail.com</div></div>
  <div class="field" style="left:22px;top:147px"><label>Phone</label><div>555 014 2290</div></div>
  <div class="field" style="left:272px;top:147px"><label>Company</label><div>Northwell Supply Co</div></div>
  <div class="field" style="left:22px;top:217px;width:401px;height:120px"><label>Enter Message</label><div>Hi, do you have a message to send?</div></div>
  <div class="btn-send"></div>
  <svg class="abs" style="left:456px;top:294px" width="30" height="30" viewBox="0 0 30 30"><path d="M27 3 L3 13 L12 16 L15 26 Z" fill="#fff"/><path d="M27 3 L12 16" stroke="#2b2b2b" stroke-width="1.5"/></svg>
</div>

<div class="info-card">
  <h4>Contact Information</h4>
  <svg class="abs" style="left:297px;top:16px" width="36" height="36" viewBox="0 0 36 36"><path d="M4 17 L18 4 L32 17 V32 H4 Z" fill="#fff"/><circle cx="18" cy="19" r="6" fill="#e01e26"/><circle cx="18" cy="19" r="2.2" fill="#fff"/></svg>
  <div class="info-row" style="top:86px;font-size:13px;line-height:19px">
    <svg width="30" height="30" viewBox="0 0 30 30" fill="none" stroke="#fff" stroke-width="1.6"><path d="M15 4 Q8 4 8 11 Q8 16 15 24 Q22 16 22 11 Q22 4 15 4 Z"/><circle cx="15" cy="11" r="3"/><path d="M4 22 L4 28 L26 28 L26 22"/></svg>
    <span>1250 Linden Row, Ashford,<br>SC 29601. USA</span>
  </div>
  <div class="info-row" style="top:157px;font-size:18px">
    <svg width="30" height="30" viewBox="0 0 30 30" fill="none" stroke="#fff" stroke-width="1.6"><rect x="4" y="5" width="8" height="21" rx="2"/><rect x="12" y="9" width="14" height="17"/><line x1="15" y1="14" x2="23" y2="14"/><line x1="15" y1="18" x2="23" y2="18"/><line x1="15" y1="22" x2="23" y2="22"/></svg>
    <span>555.014.2290</span>
  </div>
  <div class="info-row" style="top:226px;font-size:17px">
    <svg width="30" height="30" viewBox="0 0 30 30" fill="none" stroke="#fff" stroke-width="1.6"><path d="M4 13 V26 H26 V13"/><path d="M4 13 L15 21 L26 13"/><circle cx="15" cy="9" r="5"/></svg>
    <span>hello@corvalensystems.com</span>
  </div>
  <div class="social" style="left:31px" aria-label="Social profile"></div>
  <div class="social" style="left:74px;background:#fff" aria-label="Social profile"></div>
  <div class="social" style="left:117px" aria-label="Social profile"></div>
</div>

<footer class="site-footer">
  <div class="brand"><span class="brand-mark"></span>Corvalen Systems</div>
  <div class="footer-col" style="left:464px"><h5>Quick links</h5><div class="rule"></div>
    <ul><li>Home</li><li>About</li><li>Services</li><li>Blog</li><li>Contact Us</li></ul></div>
  <div class="footer-col" style="left:675px"><h5>Links</h5><div class="rule"></div>
    <ul><li>Copyright</li><li>Legal</li><li>Privacy</li><li>Accessibility</li><li>Sitemap</li></ul></div>
  <div class="footer-col" style="left:863px"><h5>Support</h5><div class="rule"></div>
    <ul><li>FAQs</li><li>Privacy Policy</li><li>Terms of Service</li><li>Request a Quote</li><li>Client Login</li></ul></div>
  <div class="footer-rule"></div>
  <div class="copyright">Copyright ©2025. All Rights Reserved</div>
  <div class="legal"><span>Terms of use</span><span>Privacy Policy</span></div>
  <svg class="to-top" width="22" height="52" viewBox="0 0 22 52" fill="none" stroke="#e01e26" stroke-width="2"><line x1="11" y1="4" x2="11" y2="50"/><polyline points="4,11 11,4 18,11"/></svg>
  <div class="ver">C44</div>
</footer>

</body>
</html>
```